Dravel

We are openıng one huntıng showroom in Riyadh? Saudi Arabia. Company name is "DRAVEL".
Our logo designed and we need Business Card Design now.
I attached DRAVEL logo below.
Front side will English and back side will be Arabic

```html
<!DOCTYPE html>
<html lang="en">
<head>
<meta charset="utf-8">
<title>Dravel Business Card</title>
<link href="https://fonts.googleapis.com/css2?family=Open+Sans:wght@400;600;700&family=Cairo:wght@400;700&display=swap" rel="stylesheet">
<style>
  :root{
    --backdrop:#2b2c2d;
    --card:#ffffff;
    --green-dark:#0e7a3e;
    --green-light:#7cb342;
    --ink:#3a3a3a;
    --divider:#c9c9c9;
  }
  *{margin:0;padding:0;box-sizing:border-box}
  html,body{width:1200px;height:892px;overflow:hidden}
  body{background:var(--backdrop);position:relative;font-family:"Open Sans",sans-serif}
  .card{position:absolute;width:560px;height:320px;background:var(--card);overflow:hidden;box-shadow:0 10px 24px rgba(0,0,0,.45)}
  .card--back{left:60px;top:60px}
  .card--front{left:580px;top:512px}
  .card__band{position:absolute;left:0;right:0;bottom:0;height:16px;background:var(--green-dark);border-top:4px solid var(--green-light)}
  .card__divider{position:absolute;left:0;top:0}
  .brand{position:absolute;left:60px;top:128px;display:flex;align-items:center;gap:12px}
  .brand__name{font-family:"Open Sans",sans-serif;font-weight:700;font-size:44px;color:var(--green-dark);letter-spacing:1px;line-height:1}
  .brand__mark{width:18px;height:18px;background:var(--green-dark)}
  .contact{position:absolute;left:370px;top:52px;color:var(--ink);font-size:13px;line-height:17px}
  .contact__name{color:var(--green-dark);font-weight:700;font-size:19px;line-height:21px;letter-spacing:.3px}
  .contact__title{color:var(--green-light);font-size:13px;margin-bottom:12px}
  .contact__address{margin-bottom:10px}
  .contact__row{display:flex;align-items:center;gap:8px}
  .contact__row svg{width:11px;height:11px;flex:none}
  .card--back .contact{font-family:"Cairo",sans-serif;direction:rtl;text-align:right;left:auto;right:40px;width:170px}
  .card--back .contact__row{direction:ltr;justify-content:flex-end;flex-direction:row-reverse;font-family:"Open Sans",sans-serif}
  .card--back .brand__name{font-family:"Cairo",sans-serif;font-size:48px}
</style>
</head>
<body>

<section class="card card--back" lang="ar">
  <svg class="card__divider" width="560" height="320"><line x1="340" y1="20" x2="380" y2="270" stroke="var(--divider)" stroke-width="1.5"/></svg>
  <div class="brand"><span class="brand__name">درافل</span><span class="brand__mark"></span></div>
  <div class="contact">
    <div class="contact__name">عمر حداد</div>
    <div class="contact__title">رئيس</div>
    <div class="contact__address">2710 طريق بالم كورت<br>الرياض 12211</div>
    <div class="contact__row"><svg viewBox="0 0 12 12"><path d="M1 4c0-2 10-2 10 0v1H8V4H4v1H1z M2 6h8l1 5H1z" fill="var(--green-dark)"/></svg>511 2064 7730</div>
    <div class="contact__row"><svg viewBox="0 0 12 12"><rect x="3" y="0.5" width="6" height="11" rx="1" fill="none" stroke="var(--green-dark)" stroke-width="1.5"/></svg>522 9413 6081</div>
    <div class="contact__row"><svg viewBox="0 0 12 12"><rect x="3" y="0" width="6" height="5" fill="var(--green-dark)"/><rect x="0" y="5" width="12" height="7" fill="var(--green-dark)"/></svg>533 7802 1459</div>
    <div class="contact__row"><svg viewBox="0 0 12 12"><rect x="0" y="2" width="12" height="8" fill="var(--green-dark)"/><path d="M0 2l6 5 6-5" stroke="#fff" fill="none"/></svg>info@dravel.com</div>
    <div class="contact__row"><svg viewBox="0 0 12 12"><circle cx="6" cy="6" r="6" fill="var(--green-dark)"/></svg>www.dravel.com</div>
  </div>
  <div class="card__band"></div>
</section>

<section class="card card--front">
  <svg class="card__divider" width="560" height="320"><line x1="330" y1="20" x2="370" y2="270" stroke="var(--divider)" stroke-width="1.5"/></svg>
  <div class="brand"><span class="brand__name">DRAVEL</span><span class="brand__mark"></span></div>
  <div class="contact">
    <div class="contact__name">OMAR HADDAD</div>
    <div class="contact__title">PRESIDENT</div>
    <div class="contact__address">2710 Palm Court Road<br>Riyadh 12211</div>
    <div class="contact__row"><svg viewBox="0 0 12 12"><path d="M1 4c0-2 10-2 10 0v1H8V4H4v1H1z M2 6h8l1 5H1z" fill="var(--green-dark)"/></svg>511 2064 7730</div>
    <div class="contact__row"><svg viewBox="0 0 12 12"><rect x="3" y="0.5" width="6" height="11" rx="1" fill="none" stroke="var(--green-dark)" stroke-width="1.5"/></svg>522 9413 6081</div>
    <div class="contact__row"><svg viewBox="0 0 12 12"><rect x="3" y="0" width="6" height="5" fill="var(--green-dark)"/><rect x="0" y="5" width="12" height="7" fill="var(--green-dark)"/></svg>533 7802 1459</div>
    <div class="contact__row"><svg viewBox="0 0 12 12"><rect x="0" y="2" width="12" height="8" fill="var(--green-dark)"/><path d="M0 2l6 5 6-5" stroke="#fff" fill="none"/></svg>info@dravel.com</div>
    <div class="contact__row"><svg viewBox="0 0 12 12"><circle cx="6" cy="6" r="6" fill="var(--green-dark)"/></svg>www.dravel.com</div>
  </div>
  <div class="card__band"></div>
</section>

</body>
</html>
```